Business Card Stationary and shirt design for Electrical Company
Corbishaw Electric LLC
Business Card Stationary and shirt design for Electrical Company - Construction
Creative Brief
Bright & Fun-filled
Owner
614 Linwood Avenue Jersey City, NJ 07305
1-855-48AMPRO
corbishawelectricllc@brivanmail.com
www.corbishawelectric-example.com
Highly rated : TradeRankr, Zorvik, NestGauge residential, commercial, industrial
Name of Business Logo web adress simple yet eye catching back (ill leave it up to the designer)

```html
<!DOCTYPE html>
<html lang="en">
<head>
<meta charset="utf-8">
<title>Corbishaw Electric LLC – Business Card</title>
<link rel="stylesheet" href="https://fonts.googleapis.com/css2?family=Montserrat:wght@400;600;700&display=swap">
<style>
  :root {
    --green: #86c440;
    --green-dark: #6fae2c;
    --navy: #1f2a44;
    --white: #ffffff;
    --grey-text: #6b6f76;
    --backdrop: #e6e7e9;
  }
  * { box-sizing: border-box; margin: 0; padding: 0; }
  html, body { width: 1200px; height: 864px; overflow: hidden; }
  body {
    background: var(--backdrop);
    font-family: "Montserrat", Arial, sans-serif;
    display: flex;
    align-items: center;
    justify-content: center;
    gap: 40px;
  }
  .card {
    position: relative;
    width: 540px;
    height: 309px;
    border-radius: 18px;
    overflow: hidden;
    box-shadow: 0 6px 18px rgba(0,0,0,0.18);
  }

  /* Back side */
  .card-back {
    background: var(--green);
    display: flex;
    flex-direction: column;
    align-items: center;
    justify-content: center;
    gap: 18px;
  }
  .brand-mark { display: flex; align-items: center; gap: 12px; }
  .brand-dot {
    width: 40px; height: 40px; border-radius: 50%;
    background: var(--navy);
    flex: none;
  }
  .brand-name {
    font-weight: 700;
    font-size: 30px;
    color: var(--white);
    letter-spacing: -0.5px;
    white-space: nowrap;
  }
  .back-web {
    font-size: 12px;
    font-weight: 600;
    letter-spacing: 3px;
    color: var(--navy);
  }

  /* Front side */
  .card-front { background: var(--white); }
  .front-brand {
    position: absolute; left: 28px; top: 112px;
    display: flex; align-items: center; gap: 8px;
  }
  .front-brand .brand-dot { width: 28px; height: 28px; }
  .front-brand .brand-name { color: var(--navy); font-size: 20px; }
  .owner-block { position: absolute; left: 56px; top: 172px; }
  .owner-company { color: var(--green-dark); font-size: 13px; font-weight: 600; }
  .owner-title { color: var(--grey-text); font-size: 10px; margin-top: 6px; }
  .contact-list {
    position: absolute; left: 322px; top: 38px;
    list-style: none;
    display: flex; flex-direction: column; gap: 6px;
  }
  .contact-item {
    display: flex; align-items: center; gap: 7px;
    font-size: 9px; color: var(--grey-text);
    white-space: nowrap;
  }
  .contact-icon {
    width: 10px; height: 10px; border-radius: 50%;
    background: var(--green); flex: none;
  }
  .front-swoosh { position: absolute; left: 0; bottom: 0; width: 540px; height: 110px; }
</style>
</head>
<body>
  <section class="card card-back">
    <div class="brand-mark">
      <span class="brand-dot"></span>
      <span class="brand-name">corbishawelectric</span>
    </div>
    <p class="back-web">www.corbishawelectric-example.com</p>
  </section>

  <section class="card card-front">
    <ul class="contact-list">
      <li class="contact-item"><span class="contact-icon"></span>614 Linwood Avenue Jersey City, NJ 07305</li>
      <li class="contact-item"><span class="contact-icon"></span>1-855-48AMPRO</li>
      <li class="contact-item"><span class="contact-icon"></span>201-555-0142</li>
      <li class="contact-item"><span class="contact-icon"></span>201-555-0187</li>
      <li class="contact-item"><span class="contact-icon"></span>201-555-0163</li>
      <li class="contact-item"><span class="contact-icon"></span>corbishawelectricllc@brivanmail.com</li>
      <li class="contact-item"><span class="contact-icon"></span>www.corbishawelectric-example.com</li>
    </ul>

    <div class="front-brand">
      <span class="brand-dot"></span>
      <span class="brand-name">corbishaw electric llc</span>
    </div>

    <div class="owner-block">
      <p class="owner-company">Corbishaw Electric LLC</p>
      <p class="owner-title">Owner</p>
    </div>

    <svg class="front-swoosh" viewBox="0 0 540 110" preserveAspectRatio="none" aria-hidden="true">
      <path d="M0 0 C 90 70, 280 110, 540 60 L540 110 L0 110 Z" fill="var(--green)"/>
      <path d="M10 110 C 200 95, 400 70, 540 20 L540 50 C 400 90, 200 110, 10 110 Z" fill="var(--navy)"/>
    </svg>
  </section>
</body>
</html>
```